Tambrel Couriers Web design

Take a look at our existing website(www.tmbrl-example.com) and design a new one, plus coding and recreate an existing logo.

```html
<!DOCTYPE html>
<html lang="en">
<head>
<meta charset="utf-8">
<title>Tambrel Couriers</title>
<link rel="stylesheet" href="https://fonts.googleapis.com/css2?family=Montserrat:wght@500;600;700&family=Lato:wght@400;700&display=swap">
<style>
:root{
  --orange:#f7871f;
  --blue:#2f6db4;
  --navy:#1d4f91;
  --dark:#222222;
  --footer:#262626;
  --grey:#6b6b6b;
  --light-grey:#8a8a8a;
  --line:#d8d8d8;
  --white:#ffffff;
}
*{box-sizing:border-box;margin:0;padding:0}
html,body{width:1200px;height:4307px;overflow:hidden}
body{position:relative;background:var(--white);font-family:"Lato",sans-serif;color:var(--grey)}
.abs{position:absolute}
h1,h2,h3,.brand{font-family:"Montserrat",sans-serif}
.btn{position:absolute;background:var(--orange);color:var(--white);font-size:11px;text-transform:uppercase;display:flex;align-items:center;justify-content:center;letter-spacing:.2px}

.topbar{left:0;top:0;width:1200px;height:36px;background:var(--dark)}
.topbar .call{left:765px;top:0;height:36px;display:flex;align-items:center;gap:6px;color:var(--white);font-size:12px}
.topbar .call b{color:var(--orange);font-weight:400}
.topbar .login{left:976px;top:0;width:112px;height:36px}

.header{left:0;top:36px;width:1200px;height:90px;background:var(--white)}
.brand{position:absolute;display:flex;align-items:center;gap:10px;font-weight:600;color:var(--grey)}
.header .brand{left:117px;top:28px;font-size:24px}
.brand i{display:block;width:14px;height:14px;background:var(--orange)}
.nav{right:112px;top:0;height:90px;display:flex;align-items:center;gap:28px;font-size:12px;color:#444}

.hero{left:0;top:126px;width:1200px;height:618px;background:linear-gradient(100deg,#2c6bb0 0%,#4a7fae 35%,#8b8f8f 60%,#c9cccf 100%)}
.hero h1{left:114px;top:222px;font-size:40px;line-height:48px;font-weight:600;color:var(--white)}
.hero .btn{left:115px;top:350px;width:134px;height:44px}

.about-img{left:114px;top:876px;width:471px;height:377px;background:linear-gradient(135deg,#b5744f,#d9d4cc 55,#8c99a8);clip-path:polygon(0 0,100% 0,100% 72%,80% 100%,0 100%)}
.about h2{left:630px;top:872px;font-size:30px;font-weight:600;color:var(--grey)}
.about .copy{left:630px;top:926px;width:456px;font-size:11px;line-height:20px;color:var(--light-grey)}
.about .copy p+p{margin-top:18px}
.about .btn{left:630px;top:1203px;width:134px;height:44px}

.services{left:0;top:1367px;width:1200px;height:784px;background:var(--orange)}
.services h2{left:0;top:78px;width:1200px;text-align:center;font-size:28px;font-weight:600;color:var(--white)}
.card{position:absolute;width:226px;height:226px;background:var(--white);border-radius:4px;display:flex;flex-direction:column;align-items:center;justify-content:center;gap:14px;text-align:center}
.card h3{font-size:18px;font-weight:500;color:#555;line-height:24px}
.card svg{width:72px;height:72px}

.sectors h2{left:0;top:2228px;width:1200px;text-align:center;font-size:30px;font-weight:500;color:var(--grey)}
.sector-img{position:absolute;top:2311px;width:313px;height:232px}
.sector h3{position:absolute;top:2570px;width:313px;text-align:center;font-size:17px;font-weight:600;color:var(--grey)}
.sector p{position:absolute;top:2598px;width:313px;text-align:center;font-size:11px;line-height:20px;color:var(--light-grey)}

.benefits{left:0;top:2734px;width:607px;height:439px;background:var(--blue)}
.benefits h2{left:110px;top:54px;font-size:30px;font-weight:600;color:var(--white)}
.benefits .sub{left:110px;top:92px;font-size:13px;color:var(--orange)}
.benefits ul{left:110px;top:128px;list-style:none;font-size:11px;color:var(--white)}
.benefits li{display:flex;align-items:center;gap:14px;height:22.4px}
.benefits-img{left:607px;top:2734px;width:593px;height:439px;background:linear-gradient(120deg,#2b5aa8,#c9a98a 55%,#e8e2da)}

.contact h2{left:0;top:3228px;width:1200px;text-align:center;font-size:30px;font-weight:500;color:var(--grey)}
.field{position:absolute;border:2px solid #e3e3e3;background:var(--white);font-size:11px;color:#b5b5b5;padding:0 18px;display:flex;align-items:center}
.field.area{align-items:flex-start;padding-top:20px}
.contact .btn{left:531px;top:3696px;width:134px;height:44px}

.footer{left:0;top:3812px;width:1200px;height:441px;background:var(--footer)}
.footer .brand{left:0;top:62px;width:1200px;justify-content:center;font-size:28px;color:#cfcfcf}
.footer h4{position:absolute;top:177px;font-family:"Montserrat",sans-serif;font-weight:500;font-size:17px;color:#bdbdbd}
.footer ul{position:absolute;top:212px;list-style:none;font-size:11px;line-height:22.4px;color:var(--white)}
.contact-info li{display:flex;align-items:center;gap:8px}
.contact-info li.indent{padding-left:16px}
.map{left:546px;top:203px;width:209px;height:131px;background:linear-gradient(135deg,#eef1f4,#dfe6ee)}
.news-input{left:809px;top:238px;width:276px;height:42px;background:var(--white);font-size:11px;font-style:italic;color:#b5b5b5;padding-left:20px;display:flex;align-items:center}
.footer .btn{left:952px;top:290px;width:133px;height:42px}
.copyright{left:0;top:4253px;width:1200px;height:54px;display:flex;align-items:center;justify-content:center;font-size:11px;color:#444}
</style>
</head>
<body>

<div class="abs topbar">
  <div class="abs call">
    <svg width="12" height="12" viewBox="0 0 24 24" fill="#fff"><path d="M6.6 10.8a15 15 0 0 0 6.6 6.6l2.2-2.2c.3-.3.7-.4 1-.2 1.1.4 2.3.6 3.6.6.6 0 1 .4 1 1V20c0 .6-.4 1-1 1A17 17 0 0 1 3 4c0-.6.4-1 1-1h3.5c.6 0 1 .4 1 1 0 1.3.2 2.5.6 3.6.1.3 0 .7-.2 1z"/></svg>
    CALL US NOW: <b>555-014-2280</b>
  </div>
  <div class="btn login">LOGIN</div>
</div>

<header class="abs header">
  <div class="brand"><i></i>Tambrel Couriers</div>
  <nav class="abs nav"><span>Home</span><span>About Us</span><span>Services</span><span>Rates</span><span>Customer Benefits</span><span>Contact us</span></nav>
</header>

<section class="abs hero" role="img" aria-label="Branded white courier van driving on a mountain road">
  <h1 class="abs">Quick and Responsive<br>Deliveries Globally</h1>
  <div class="btn">Read More</div>
</section>

<section class="about">
  <div class="abs about-img" role="img" aria-label="Courier handing a parcel to a customer beside a delivery van"></div>
  <h2 class="abs">About Us</h2>
  <div class="abs copy">
    <p>Welcome to Tambrel Couriers. We are committed to providing professional messenger services to cater for the most important, emergency and time sensitive deliveries valuable to your company.<br>Our services range from scheduled local and long distance, same day to all types of On Demand services.</p>
    <p>Our goal is to become a leader by showing reliability, integrity as well as competitive pricing.</p>
    <p>Our company is licensed, bonded and fully insured with commercial grade insurance. Our personnel are professional, uniformed and our vehicles are identified and all have commercial insurance.</p>
  </div>
  <div class="btn">Read More</div>
</section>

<section class="abs services">
  <h2 class="abs">Our Services</h2>
  <div class="card" style="left:112px;top:160px">
    <svg viewBox="0 0 64 64" fill="none" stroke="#2f6db4" stroke-width="3"><path d="M18 8h20l10 10v38H18z"/><path d="M24 28h18M24 36h18M24 44h18" stroke="#f7871f"/></svg>
    <h3>On-Demand</h3></div>
  <div class="card" style="left:361px;top:160px">
    <svg viewBox="0 0 64 64" fill="none" stroke="#2f6db4" stroke-width="3"><rect x="26" y="20" width="24" height="22"/><path d="M26 28h24" stroke="#f7871f"/><path d="M8 24h12M4 32h14M8 40h12" stroke="#f7871f"/></svg>
    <h3>Rush</h3></div>
  <div class="card" style="left:612px;top:160px">
    <svg viewBox="0 0 64 64" fill="none" stroke="#2f6db4" stroke-width="3"><path d="M14 20h28v22H14zM42 28h10l6 8v6H42z"/><circle cx="22" cy="46" r="4" stroke="#f7871f"/><circle cx="50" cy="46" r="4" stroke="#f7871f"/><path d="M4 26h8M2 34h10" stroke="#f7871f"/></svg>
    <h3>Regular Delivery</h3></div>
  <div class="card" style="left:861px;top:160px">
    <svg viewBox="0 0 64 64" fill="none" stroke-width="3"><path d="M12 30a22 22 0 1 1 8 18" stroke="#2f6db4"/><path d="M36 20v14l8 6" stroke="#f7871f"/><text x="6" y="52" font-size="18" font-family="Montserrat,sans-serif" font-weight="700" fill="#2f6db4" stroke="none">24</text></svg>
    <h3>After Hours Delivery</h3></div>
  <div class="card" style="left:112px;top:421px">
    <svg viewBox="0 0 64 64" fill="none" stroke-width="3"><circle cx="38" cy="34" r="18" stroke="#2f6db4"/><path d="M38 24v10l6 4M34 10h8" stroke="#f7871f"/><path d="M4 28h12M2 36h12M6 44h10" stroke="#f7871f"/></svg>
    <h3>Same Day Service</h3></div>
  <div class="card" style="left:361px;top:421px">
    <svg viewBox="0 0 64 64" fill="none" stroke-width="3"><rect x="8" y="12" width="44" height="36" rx="3" stroke="#2f6db4"/><path d="M8 22h44" stroke="#2f6db4"/><path d="M16 30h4M26 30h4M36 30h4M16 38h4M26 38h4" stroke="#f7871f"/><circle cx="48" cy="46" r="9" stroke="#2f6db4" fill="#fff"/><path d="M44 46h8M49 43l3 3-3 3" stroke="#2f6db4"/></svg>
    <h3>Next Day/Overnight<br>Delivery</h3></div>
  <div class="card" style="left:612px;top:421px">
    <svg viewBox="0 0 64 64" fill="none" stroke-width="3"><path d="M8 56V22L32 8l24 14v34" stroke="#2f6db4"/><rect x="22" y="34" width="20" height="22" stroke="#f7871f"/><path d="M22 34l20 22M42 34L22 56" stroke="#f7871f"/></svg>
    <h3>Warehousing and<br>Distribution</h3></div>
  <div class="card" style="left:861px;top:421px">
    <svg viewBox="0 0 64 64" fill="none" stroke-width="3"><rect x="6" y="12" width="42" height="36" rx="3" stroke="#2f6db4"/><path d="M6 22h42M16 6v10M38 6v10" stroke="#2f6db4"/><path d="M14 30h4M24 30h4M14 38h4" stroke="#f7871f"/><circle cx="46" cy="44" r="11" stroke="#f7871f" fill="#fff"/><path d="M46 38v6h5" stroke="#f7871f"/></svg>
    <h3>Scheduled Services</h3></div>
</section>

<section class="sectors">
  <h2 class="abs">Tambrel will service the following</h2>
  <div class="sector">
    <div class="sector-img" style="left:112px;background:linear-gradient(135deg,#c8d2d8,#e9eef0 50%,#9fb0ba)" role="img" aria-label="Medical staff in a hospital corridor"></div>
    <h3 style="left:112px">Hospital &amp; Medical Care</h3>
    <p style="left:112px">Home Deliveries, Pharmaceuticals and Critical Routes.</p>
  </div>
  <div class="sector">
    <div class="sector-img" style="left:444px;background:linear-gradient(135deg,#d9ddd6,#9ea79c 50%,#e1e4de)" role="img" aria-label="Close view of banknotes"></div>
    <h3 style="left:444px">Banking &amp; Brokerage</h3>
    <p style="left:444px">Overnight Deliveries, Mortgage Documents,<br>Interoffice Routes.</p>
  </div>
  <div class="sector">
    <div class="sector-img" style="left:774px;background:linear-gradient(135deg,#2a2a2a,#111 60%,#5a4324);clip-path:polygon(0 0,100% 0,100% 80%,86% 100%,0 100%)" role="img" aria-label="Judge's gavel on a dark desk"></div>
    <h3 style="left:774px">Legal</h3>
    <p style="left:774px">Legal, Administrative and also deliveries associated<br>with Manufacturing.</p>
  </div>
</section>

<section class="abs benefits">
  <h2 class="abs">Customer Benefits</h2>
  <div class="abs sub">A short list of benefits our customers receive include:</div>
  <ul class="abs">
    <li><svg width="11" height="9" viewBox="0 0 11 9"><path d="M1 4.5l3 3L10 1" fill="none" stroke="#f7871f" stroke-width="2"/></svg>Money back guaranteed if your package is not delivered on time</li>
    <li><svg width="11" height="9" viewBox="0 0 11 9"><path d="M1 4.5l3 3L10 1" fill="none" stroke="#f7871f" stroke-width="2"/></svg>Free waiting time</li>
    <li><svg width="11" height="9" viewBox="0 0 11 9"><path d="M1 4.5l3 3L10 1" fill="none" stroke="#f7871f" stroke-width="2"/></svg>All our services are guaranteed</li>
    <li><svg width="11" height="9" viewBox="0 0 11 9"><path d="M1 4.5l3 3L10 1" fill="none" stroke="#f7871f" stroke-width="2"/></svg>Pickup within 15 to 30 mins.of your call or sooner</li>
    <li><svg width="11" height="9" viewBox="0 0 11 9"><path d="M1 4.5l3 3L10 1" fill="none" stroke="#f7871f" stroke-width="2"/></svg>First 100lbs. are free</li>
    <li><svg width="11" height="9" viewBox="0 0 11 9"><path d="M1 4.5l3 3L10 1" fill="none" stroke="#f7871f" stroke-width="2"/></svg>State of the art courier software system</li>
    <li><svg width="11" height="9" viewBox="0 0 11 9"><path d="M1 4.5l3 3L10 1" fill="none" stroke="#f7871f" stroke-width="2"/></svg>Online order entry</li>
    <li><svg width="11" height="9" viewBox="0 0 11 9"><path d="M1 4.5l3 3L10 1" fill="none" stroke="#f7871f" stroke-width="2"/></svg>Online order tracking</li>
    <li><svg width="11" height="9" viewBox="0 0 11 9"><path d="M1 4.5l3 3L10 1" fill="none" stroke="#f7871f" stroke-width="2"/></svg>Signature capturing</li>
    <li><svg width="11" height="9" viewBox="0 0 11 9"><path d="M1 4.5l3 3L10 1" fill="none" stroke="#f7871f" stroke-width="2"/></svg>Be able to see invoices online</li>
    <li><svg width="11" height="9" viewBox="0 0 11 9"><path d="M1 4.5l3 3L10 1" fill="none" stroke="#f7871f" stroke-width="2"/></svg>Be able to print shipping labels</li>
  </ul>
</section>
<div class="abs benefits-img" role="img" aria-label="Courier in a blue uniform having a customer sign for a parcel"></div>

<section class="contact">
  <h2 class="abs">Contact Us</h2>
  <div class="field" style="left:277px;top:3295px;width:313px;height:50px">Full Name</div>
  <div class="field" style="left:602px;top:3295px;width:314px;height:50px">Phone</div>
  <div class="field" style="left:277px;top:3355px;width:639px;height:50px">Email</div>
  <div class="field" style="left:277px;top:3417px;width:313px;height:50px">Street Addres</div>
  <div class="field" style="left:602px;top:3417px;width:314px;height:50px">City Or Town</div>
  <div class="field" style="left:277px;top:3479px;width:313px;height:50px">State</div>
  <div class="field" style="left:602px;top:3479px;width:314px;height:50px">Zip Code</div>
  <div class="field area" style="left:277px;top:3539px;width:639px;height:131px">Regarding</div>
  <div class="btn">Submit Now</div>
</section>

<footer class="abs footer">
  <div class="brand"><i></i>Tambrel Couriers</div>
  <h4 style="left:110px">Quick Links</h4>
  <ul style="left:110px"><li>Home</li><li>About Us</li><li>Services</li><li>Rates</li><li>Customer Benefits</li><li>Contact us</li></ul>
  <h4 style="left:304px">Contact info.</h4>
  <ul class="contact-info" style="left:304px">
    <li><svg width="8" height="11" viewBox="0 0 8 11"><path d="M4 0a4 4 0 0 1 4 4c0 3-4 7-4 7S0 7 0 4a4 4 0 0 1 4-4z" fill="#f7871f"/></svg>412 Harlow Ave.</li>
    <li class="indent">Linden, NY 14099</li>
    <li><svg width="8" height="8" viewBox="0 0 8 8"><rect width="8" height="8" fill="#f7871f"/></svg>P.O. Box 5180 Linden, NY 14098</li>
    <li><svg width="9" height="9" viewBox="0 0 24 24" fill="#f7871f"><path d="M6.6 10.8a15 15 0 0 0 6.6 6.6l2.2-2.2c.3-.3.7-.4 1-.2 1.1.4 2.3.6 3.6.6.6 0 1 .4 1 1V20c0 .6-.4 1-1 1A17 17 0 0 1 3 4c0-.6.4-1 1-1h3.5c.6 0 1 .4 1 1 0 1.3.2 2.5.6 3.6.1.3 0 .7-.2 1z"/></svg>555-013-4471</li>
    <li><svg width="9" height="9" viewBox="0 0 10 10"><rect x="1" y="3" width="8" height="6" fill="#f7871f"/><rect x="2" y="0" width="6" height="3" fill="#f7871f"/></svg>555-016-9305</li>
    <li><svg width="10" height="8" viewBox="0 0 10 8"><rect width="10" height="8" fill="#f7871f"/><path d="M0 0l5 4 5-4" fill="none" stroke="#262626"/></svg>info@tmbrl-example.com</li>
  </ul>
  <h4 style="left:545px">Location</h4>
  <div class="abs map" role="img" aria-label="Street map showing the office location"></div>
  <h4 style="left:809px">Newsletter</h4>
  <div class="abs news-input">Email Address</div>
  <div class="btn">Submit Now</div>
</footer>

<div class="abs copyright">Copyright © 2021 Tambrel Couriers</div>

</body>
</html>
```